Single-page, simple & clean, departure board web app

TrellWick.com provides easy to use train schedule information in Chicago, IL between downtown and Hyde Park. The site has been around for about 3 years and the design has not changed since the weekend hackathon at which it was created. Now, it has a solid user base and is in dire need of a fresh design.
The design should be super-clean and intuitive. It is used by the type of people who love the style and personality of sites like Dazzleferr. The design should incorporate the maroon color that is used extensively on the existing site. The main features are (1) the train depart times, (2) the fact that different stations can be selected as departure/arrival, (3) the fact that a user can click "earlier trains" or "later trains" to quickly scan the times.
This is a single-page web app that displays static content. The design should reflect that 100% of the users time is spent on the single page. There is no "sign up" process or external aspect. All focus should be used to design the best possible display of train times.
Target Market(s)
24-30 yr old, middle to upper income, opinionated, heavily international
Look and feel
Each slider illustrates characteristics of the customer's brand and the style your logo design should communicate.

```html
<!DOCTYPE html>
<html lang="en">
<head>
<meta charset="utf-8">
<title>TrellWick – Train Times</title>
<link rel="stylesheet" href="https://fonts.googleapis.com/css2?family=Bebas+Neue&family=Lato:wght@400;700;900&display=swap">
<style>
:root{
  --page-bg:#dcdcdc;
  --card-bg:#f5f5f5;
  --maroon:#9b2a3e;
  --maroon-light:#b33b50;
  --maroon-dark:#7c1729;
  --panel-bg:#e8e8e8;
  --tabbar-top:#8c8c8c;
  --tabbar-bottom:#6c6c6c;
  --ink:#2c2c2c;
  --muted:#8c8c8c;
  --faint:#bdbdbd;
  --label-red:#b51f3a;
  --rule:#e3e3e3;
  --white:#ffffff;
}
*{box-sizing:border-box;margin:0;padding:0}
html,body{width:1200px;height:873px;overflow:hidden}
body{background:var(--page-bg);font-family:"Lato",sans-serif;color:var(--ink)}
.stage{position:relative;width:1100px;height:800px;transform:scale(1.090909);transform-origin:0 0}
.app{position:absolute;left:70px;top:50px;width:960px;height:700px;background:var(--card-bg);border-radius:8px;box-shadow:0 14px 14px -8px rgba(0,0,0,.35)}
.app-header{position:absolute;left:0;top:0;width:960px;height:80px;border-radius:8px 8px 0 0;background:linear-gradient(#b23a4f,#8d1d31);border-bottom:1px solid #6e1022}
.brand{position:absolute;left:30px;top:22px;font-weight:900;font-size:30px;color:var(--white);letter-spacing:.2px}
.direction{position:absolute;left:540px;top:21px;width:400px;height:40px;display:flex;border:1px solid #6a0f20;border-radius:4px;overflow:hidden}
.direction span{flex:1;display:flex;align-items:center;justify-content:center;font-weight:700;font-size:15px;color:var(--white)}
.direction .is-active{background:linear-gradient(#7a1528,#8c1f33);box-shadow:inset 0 2px 4px rgba(0,0,0,.3)}
.direction .option{background:linear-gradient(#bb4559,#a2304a);border-left:1px solid #6a0f20}
.hint{position:absolute;font-weight:900;font-size:14px;letter-spacing:-.3px}
.hint svg{position:absolute;width:28px;height:28px}
.hint-light{color:var(--white)}
.hint-dark{color:#111}
.board{position:absolute;left:20px;top:101px;width:920px;height:500px;background:var(--panel-bg);border:1px solid #cfcfcf;border-radius:5px;overflow:hidden}
.stations{position:absolute;left:0;top:0;width:920px;height:58px;background:linear-gradient(var(--tabbar-top),var(--tabbar-bottom))}
.station-tab{position:absolute;top:18px;width:190px;height:40px;border-radius:4px 4px 0 0;display:flex;align-items:center;justify-content:center;font-size:15px;color:#7a7a7a;background:linear-gradient(#fafafa,#e3e3e3)}
.station-tab.is-active{background:var(--white);color:#333}
.trains{position:absolute;left:0;top:58px;width:920px;height:50px;background:linear-gradient(#ffffff,#f1f1f1);border-bottom:1px solid #d8d8d8}
.train-pill{position:absolute;top:12px;width:160px;height:29px;border-radius:15px;border:1px solid #e2e2e2;background:linear-gradient(#ffffff,#f3f3f3);display:flex;align-items:center;justify-content:center;font-weight:700;font-size:14px;color:var(--faint)}
.train-pill.is-active{color:#2a2a2a;background:linear-gradient(#f6f6f6,#e9e9e9)}
.schedule{position:absolute;left:20px;top:129px;width:880px;height:340px;background:var(--white);border-radius:4px;overflow:hidden;box-shadow:0 1px 2px rgba(0,0,0,.12)}
.stop{position:relative;border-bottom:1px solid var(--rule)}
.stop-time{position:absolute;left:27px;font-family:"Bebas Neue",sans-serif;font-size:39px;color:#2b2b2b;letter-spacing:-.5px}
.stop-time small{font-size:39px;color:var(--muted);margin-left:4px}
.stop-info{position:absolute;left:233px}
.stop-label{display:block;font-size:11px;color:var(--label-red);text-transform:uppercase;letter-spacing:.2px}
.stop-name{display:block;font-size:18px;font-weight:700;color:#333;margin-top:1px}
.paging{position:absolute;left:0;top:295px;width:880px;height:45px;background:var(--maroon);display:flex;align-items:center;justify-content:space-between;padding:0 22px 0 27px;font-weight:700;font-size:13px;color:var(--white)}
.paging a{display:flex;align-items:center;gap:12px;color:inherit;text-decoration:none}
.page-footer{position:absolute;left:0;top:632px;width:960px;text-align:center;font-size:13px;line-height:17px;color:#555}
</style>
</head>
<body>
<div class="stage">
  <main class="app">
    <header class="app-header">
      <div class="brand">TrellWick</div>
      <nav class="direction">
        <span class="is-active">To Kestrel Hall</span>
        <span class="option">To Downtown</span>
      </nav>
      <div class="hint hint-light" style="left:496px;top:21px">CLICK<span style="margin-left:3px">1</span>
        <svg style="left:28px;top:-6px" viewBox="0 0 28 28"><circle cx="14" cy="14" r="11" fill="none" stroke="#bbb" stroke-width="3.5"/></svg>
      </div>
    </header>

    <section class="board">
      <div class="stations">
        <div class="station-tab is-active" style="left:19px">From&nbsp; Millenium</div>
        <div class="station-tab" style="left:229px">From&nbsp; Van Buren</div>
        <div class="station-tab" style="left:439px">From 11th</div>
      </div>
      <div class="trains">
        <div class="train-pill is-active" style="left:19px">Train 103</div>
        <div class="train-pill" style="left:200px">Train 305</div>
        <div class="train-pill" style="left:377px">Train 105</div>
      </div>

      <div class="schedule">
        <div class="stop" style="height:68px">
          <div class="stop-time" style="top:17px">05:15<small>AM</small></div>
          <div class="stop-info" style="top:20px"><span class="stop-label">Departure from</span><span class="stop-name">Millenium Station</span></div>
        </div>
        <div class="stop" style="height:74px">
          <div class="stop-time" style="top:19px">05:30<small>AM</small></div>
          <div class="stop-info" style="top:20px"><span class="stop-label">Arrive at</span><span class="stop-name">51st - 53rd Street</span></div>
        </div>
        <div class="stop" style="height:76px">
          <div class="stop-time" style="top:19px">05:31<small>AM</small></div>
          <div class="stop-info" style="top:20px"><span class="stop-label">Arrive at</span><span class="stop-name">55th - 56th - 57th Street</span></div>
        </div>
        <div class="stop" style="height:77px;border-bottom:0">
          <div class="stop-time" style="top:20px">05:33<small>AM</small></div>
          <div class="stop-info" style="top:20px"><span class="stop-label">Arrive at</span><span class="stop-name">59th Street</span></div>
        </div>
        <div class="paging">
          <a href="#earlier">
            <svg width="24" height="19" viewBox="0 0 24 19"><path d="M7 0H24V19H7L0 9.5Z" fill="#6b1020"/></svg>
            Earlier Trains
          </a>
          <a href="#later">
            Later Trains
            <svg width="24" height="19" viewBox="0 0 24 19"><path d="M0 0H17L24 9.5L17 19H0Z" fill="#6b1020"/></svg>
          </a>
        </div>
      </div>

      <div class="hint hint-dark" style="left:131px;top:9px">CLICK<span style="margin-left:3px">2</span>
        <svg style="left:32px;top:-6px" viewBox="0 0 28 28"><circle cx="14" cy="14" r="11" fill="none" stroke="#aaa" stroke-width="3.5"/></svg>
      </div>
      <div class="hint hint-dark" style="left:1px;top:60px">CLICK<span style="margin-left:3px">3</span>
        <svg style="left:32px;top:-6px" viewBox="0 0 28 28"><circle cx="14" cy="14" r="11" fill="none" stroke="#aaa" stroke-width="3.5"/></svg>
      </div>
    </section>

    <footer class="page-footer">
      Train Schedule Last Updated: January 15, 2012<br>
      Terms and Conditions of Use | Questions or Comments
    </footer>
  </main>
</div>
</body>
</html>
```